A Writer With A Website (Writes action/mysteries with a touch of romance thrown in)

I need a website. I am an unpublished writer. I own a domain and tried a bit to design one in Wordpress. I would like to be able to change out pictures, blog, and receive email. My fav color is orange (but not necessary in website) I like the font "Hello Stockholm" Probably 4 or five different pages. Attached is a poor scan of a business card.
Updates

Had a recent death in the family, my inspiration to get the site designed and also the reason I may need a few days.

I write books action mysteries. So far all take place in Wyoming. I realize there was not much info given. Pages: Home, Looking for representation, recommended reading and other things I like, Mirabel (a page dedicated to my daughter who just passed away), and other useful links. Probably shorter ways to say those, but you get the idea.

Thanks for the designs submitted. I know I gave very little direction. There are a few authors who write in Wyoming who are popular, RT Haskell, Dwight Fenner (Ashcroft Saga) I would argue that the main character in any of their books is Wyoming, or the West. No cliches. Cowboy hats, horses, not so good. For those outside the US, maybe do a serch on Wyoming and look at the pictures. I have photo's for possible use in my design, will post them tonight. Thanks all. -k-

I am not sure how much info gets added, how much the designer does and how I fill in the "blanks". Here is partial text for the "Mirabel" page: Over the years, our daughters’ friends overlapped one another and two or three became like daughters to Loreen and me. Some even became our friends as they grew into adulthood. One had a father who tried to committed suicide multiple times. After one attempt she asked him, “why?” He said, “I am glad you can’t understand why, only someone who can travel to that dark a place can understand why”. He was eventually successful. She shared that story with us on August 14th when our daughter Mirabel found that dark place in herself and took her life. We found a suicide note, then her body, then everything went into a fog. An hour or so later, my wife and I stood on the front lawn after the police interviews and watched as the corner slide a covered corpse into the white SUV with darkened windows. We stood there as the rain began to fall, and the sky sobbed with us. As they closed the back of the coroner’s Suburban, the rain fell harder and harder and a fireman guided us back into the house that will never be the same for us.

Target Market(s)

Currently trying to get an agent, this is to look like I have followers.

Number of Pages Required

5+ page

Font styles to use
Serif

Colors
f68e4e

Requirements
Nice to have
• I like orange (more of a burnt orange color) I am a big fan of Matthias Dorrel. A "feel" like that might be nice. I am from Wyoming, That rugged western culture shows up in all my writing.
Should not have
• Western Cliche,

```html
<!DOCTYPE html>
<html lang="en">
<head>
<meta charset="utf-8">
<title>W T Hollis — Author</title>
<link rel="stylesheet" href="https://fonts.googleapis.com/css2?family=Kaushan+Script&family=Cinzel:wght@400&family=Open+Sans:wght@400;600;700&family=Roboto+Slab:wght@700&display=swap">
<style>
:root{
  --orange:#ef8a4f;
  --orange-deep:#d9703a;
  --brown:#3a2a1f;
  --brown-mid:#4a3526;
  --ink:#2b2b2b;
  --muted:#666;
  --line:#e2e2e2;
  --white:#fff;
}
*{box-sizing:border-box;margin:0;padding:0}
html,body{width:1200px;height:3750px;overflow:hidden;background:var(--white)}
body{font-family:"Open Sans",sans-serif;color:var(--ink)}
.canvas{position:relative;width:1200px;height:3750px;overflow:hidden}
.abs{position:absolute}
.script{font-family:"Kaushan Script",cursive}
.btn{position:absolute;display:inline-block;background:var(--orange);color:var(--white);font-size:12px;font-weight:700;letter-spacing:.5px;text-transform:uppercase;padding:0 22px;height:34px;line-height:34px;border-radius:3px}
.btn.brown{background:#7a5236}
/* header */
.site-header{position:absolute;left:0;top:0;width:1200px;height:75px;background:var(--white)}
.brand{position:absolute;left:190px;top:22px;font-family:"Kaushan Script",cursive;font-size:24px;color:var(--ink)}
.brand-dot{position:absolute;left:305px;top:24px;width:28px;height:28px;border-radius:50%;background:#8a7a6a}
.follow-tab{position:absolute;left:805px;top:0;width:245px;height:22px;background:var(--brown);color:#fff;font-size:11px;line-height:22px;padding-left:18px;border-radius:0 0 0 8px}
.follow-tab span{display:inline-block;width:9px;height:9px;border-radius:50%;background:#fff;margin-left:7px;vertical-align:middle}
.main-nav{position:absolute;left:480px;top:42px;display:flex;gap:0}
.main-nav a{font-family:"Kaushan Script",cursive;font-size:16px;color:var(--ink);text-decoration:none;width:124px;text-align:center;border-right:1px solid var(--line)}
.main-nav a:last-child{border-right:0}
.main-nav a.active{text-decoration:underline;text-underline-offset:6px}
/* hero */
.hero-photo{position:absolute;left:0;top:75px;width:1200px;height:575px;background:linear-gradient(180deg,#7e6a7a 0%,#c98a55 30%,#e8a25a 42%,#5b4a44 58%,#6a5a3c 66%,#b58458 74%,#d9a876 100%)}
.hero-book{position:absolute;left:175px;top:190px;width:280px;height:500px;background:linear-gradient(160deg,#3c6fa8,#1d4e86 60%,#2a5f95);box-shadow:0 14px 24px rgba(0,0,0,.35)}
.hero-title{position:absolute;left:585px;top:265px;font-family:"Cinzel",serif;font-size:62px;color:var(--white);letter-spacing:2px}
.hero-text{position:absolute;left:585px;top:350px;width:460px;font-size:13px;line-height:18px;color:var(--white)}
.hero-dots{position:absolute;left:590px;top:460px;width:40px;height:4px;border-top:2px solid #fff}
/* about */
.about-name{position:absolute;left:210px;top:722px;font-size:38px;color:var(--ink)}
.about-rule{position:absolute;left:210px;top:782px;width:90px;height:3px;background:var(--orange)}
.about-text{position:absolute;left:210px;top:805px;width:480px;font-size:12px;line-height:20px;color:#444}
.photo-stack{position:absolute;width:210px;height:240px;background:#fff;box-shadow:0 6px 16px rgba(0,0,0,.25)}
.photo-stack .fill{position:absolute;left:10px;top:10px;right:10px;bottom:10px}
/* books */
.books-band{position:absolute;left:0;top:1083px;width:1200px;height:312px;background:linear-gradient(180deg,var(--orange),var(--orange-deep))}
.section-title{position:absolute;left:0;width:1200px;text-align:center;font-size:30px}
.book-card{position:absolute;width:200px;text-align:center}
.book-cover{width:200px;height:270px;box-shadow:0 10px 20px rgba(0,0,0,.35)}
.book-name{margin-top:30px;font-family:"Roboto Slab",serif;font-size:15px;color:var(--ink);text-transform:uppercase}
.read-more{margin-top:10px;font-size:11px;font-weight:700;text-transform:uppercase;color:var(--ink)}
.chev{position:absolute}
/* video */
.video-band{position:absolute;left:0;top:1670px;width:1200px;height:280px;background:linear-gradient(180deg,var(--brown),var(--brown-mid))}
.video-frame{position:absolute;left:217px;top:1742px;width:770px;height:375px;background:#fff;padding:5px;box-shadow:0 8px 20px rgba(0,0,0,.25)}
.video-frame .fill{width:100%;height:100%;background:linear-gradient(180deg,#a9c3d8 0%,#d0dce6 30%,#7f8a86 45%,#3f5a48 60%,#4b6f82 75%,#3d5e74 100%)}
/* testimonials */
.title-rule{position:absolute;height:1px;background:var(--line)}
.avatar{position:absolute;border-radius:50%;background:#bdb6ae}
.avatar.main{border:4px solid var(--orange);background:#a49b91}
.reviewer{position:absolute;left:0;width:1200px;text-align:center}
/* mirabel */
.tribute{position:absolute;left:0;top:2487px;width:1200px;height:373px;background:var(--brown)}
.tribute-text{position:absolute;left:445px;top:2620px;width:560px;font-size:12px;line-height:20px;color:#e8dfd6}
/* blog */
.blog-card{position:absolute;top:3032px;width:242px;height:318px;background:#fff;box-shadow:0 2px 8px rgba(0,0,0,.12)}
.blog-card .thumb{height:155px}
.blog-date{position:absolute;left:60px;top:140px;width:120px;height:26px;line-height:26px;background:var(--orange);color:#fff;font-size:9px;font-weight:700;text-align:center;text-transform:uppercase}
.blog-title{position:absolute;left:18px;top:180px;width:206px;font-size:12px;line-height:16px;color:var(--ink)}
.blog-excerpt{position:absolute;left:18px;top:222px;width:206px;font-size:10px;line-height:15px;color:#888}
.blog-more{position:absolute;left:18px;top:292px;font-size:10px;color:var(--orange);text-decoration:underline}
/* footer */
.site-footer{position:absolute;left:0;top:3462px;width:1200px;height:288px;background:linear-gradient(180deg,#3d2c20,#2f2219)}
.foot-title{position:absolute;top:3500px;font-size:20px;color:#fff}
.foot-list{position:absolute;top:3548px;list-style:none;font-size:11px;color:#e6ddd4}
.foot-list li{height:20px}
.foot-list li::before{content:"›";margin-right:10px}
.contact-row{position:absolute;left:362px;font-size:11px;color:#fff;font-weight:600;line-height:16px}
.contact-ico{position:absolute;left:-40px;top:0;width:24px;height:24px;border-radius:50%;background:var(--orange)}
.field{position:absolute;left:620px;width:180px;height:28px;border:1px solid #7a6655;color:#cdbfb2;font-size:10px;line-height:26px;padding-left:10px}
.copyright{position:absolute;left:0;top:3718px;width:1200px;text-align:center;font-size:9px;font-weight:700;color:#d8cbbd;letter-spacing:.5px}
.social-dot{position:absolute;top:3640px;width:22px;height:22px;border-radius:50%;background:#fff}
</style>
</head>
<body>
<div class="canvas">

  <!-- Header -->
  <header class="site-header">
    <div class="brand">W T Hollis</div>
    <div class="brand-dot"></div>
    <div class="follow-tab">Follow Me: <span></span><span></span><span></span><span></span></div>
    <nav class="main-nav">
      <a class="active">Home</a><a>About Me</a><a>Books</a><a>Blog</a><a>Contact Us</a>
    </nav>
  </header>

  <!-- Hero -->
  <div class="hero-photo" role="img" aria-label="Wyoming mountain range at sunset above a wooden deck"></div>
  <div class="hero-book" role="img" aria-label="Stacked hardcover books with a mountain lake cover"></div>
  <h1 class="hero-title">MIRABEL</h1>
  <p class="hero-text">Lorem ipsum dolor sit amet, consectetuer adipiscing elit, sed diam nonummy nibh euismod tincidunt ut laoreet dolore magna.</p>
  <span class="btn" style="left:585px;top:400px">Learn More</span>
  <div class="hero-dots"></div>

  <!-- About -->
  <h2 class="about-name script">Warren T. Hollis</h2>
  <div class="about-rule"></div>
  <p class="about-text">Lorem ipsum dolor sit amet, consectetuer adipiscing elit, sed diam nonummy nibh euismod tincidunt ut laoreet dolore magna aliquam erat volutpat. Ut wisi enim ad minim veniam, quis nostrud exerci tation ullamcorper suscipit lobortis nisl ut aliquip ex ea commodo consequat. Duis autem vel eum iriure dolor in hendrerit in vulputate velit esse molestie consequat, vel illum dolore eu feugiat nulla facilisis at vero eros et accumsan et iusto odio dignissim qui blandit praesent luptatum zzril delenit augue duis dolore te feugait nulla facilisi.</p>
  <span class="btn" style="left:210px;top:995px">Read More</span>
  <div class="photo-stack" style="left:700px;top:735px;transform:rotate(-8deg)"><div class="fill" style="background:#6b6258"></div></div>
  <div class="photo-stack" style="left:720px;top:740px;transform:rotate(5deg)"><div class="fill" role="img" aria-label="Author standing outdoors in a grey sweater" style="background:linear-gradient(180deg,#5a5f64,#7a8088 50%,#4d5a70)"></div></div>

  <!-- Books -->
  <div class="books-band"></div>
  <h2 class="section-title script" style="top:1128px;color:#fff">Some Of My Books</h2>
  <div class="abs" style="left:550px;top:1180px;width:100px;height:1px;background:rgba(255,255,255,.6)"></div>
  <svg class="chev" style="left:158px;top:1295px" width="16" height="26" viewBox="0 0 16 26"><path d="M13 2 3 13l10 11" fill="none" stroke="rgba(255,255,255,.7)" stroke-width="3"/></svg>
  <svg class="chev" style="left:1025px;top:1295px" width="16" height="26" viewBox="0 0 16 26"><path d="M3 2l10 11L3 24" fill="none" stroke="rgba(255,255,255,.7)" stroke-width="3"/></svg>
  <div class="book-card" style="left:215px;top:1225px">
    <div class="book-cover" role="img" aria-label="Romance novel cover in soft pink tones" style="background:linear-gradient(180deg,#e8d4dc,#c98aa4 60%,#8a5a7a)"></div>
    <div class="book-name">Duis Autem Vel</div><div class="read-more">Read More »</div>
  </div>
  <div class="book-card" style="left:500px;top:1225px">
    <div class="book-cover" role="img" aria-label="Action thriller cover in fiery orange" style="background:linear-gradient(180deg,#5a2a14,#b8521e 50%,#3a1c10)"></div>
    <div class="book-name">Duis Autem Vel</div><div class="read-more">Read More »</div>
  </div>
  <div class="book-card" style="left:790px;top:1225px">
    <div class="book-cover" role="img" aria-label="Crime mystery cover in dark blue and black" style="background:linear-gradient(180deg,#1c2630,#2e3c4a 50%,#141a20)"></div>
    <div class="book-name">Duis Autem Vel</div><div class="read-more">Read More »</div>
  </div>
  <span class="btn" style="left:548px;top:1580px">View All</span>

  <!-- Video -->
  <div class="video-band"></div>
  <div class="video-frame"><div class="fill" role="img" aria-label="Kayaker on a mountain lake beneath snowy peaks"></div></div>
  <svg class="abs" style="left:575px;top:1900px" width="50" height="50" viewBox="0 0 50 50"><circle cx="25" cy="25" r="24" fill="#ef8a4f"/><path d="M20 15v20l16-10z" fill="#fff"/></svg>

  <!-- Testimonials -->
  <h2 class="section-title script" style="top:2175px;color:var(--ink)">Reader Say About Books</h2>
  <div class="title-rule" style="left:380px;top:2232px;width:440px"></div>
  <div class="avatar" style="left:365px;top:2282px;width:58px;height:58px"></div>
  <div class="avatar" style="left:445px;top:2282px;width:58px;height:58px"></div>
  <svg class="abs" style="left:520px;top:2303px" width="20" height="14" viewBox="0 0 20 14"><path d="M19 7H2M7 2 2 7l5 5" fill="none" stroke="#999" stroke-width="1.5"/></svg>
  <div class="avatar main" style="left:555px;top:2262px;width:90px;height:90px"></div>
  <svg class="abs" style="left:660px;top:2303px" width="20" height="14" viewBox="0 0 20 14"><path d="M1 7h17M13 2l5 5-5 5" fill="none" stroke="#999" stroke-width="1.5"/></svg>
  <div class="avatar" style="left:697px;top:2282px;width:58px;height:58px"></div>
  <div class="avatar" style="left:777px;top:2282px;width:58px;height:58px"></div>
  <div class="reviewer" style="top:2366px;font-size:13px;font-weight:700">DANIEL <span style="font-weight:400">ROURKE</span></div>
  <div class="reviewer" style="top:2386px;font-size:10px;font-style:italic;color:#777">(Businessman)</div>
  <div class="reviewer" style="top:2406px;font-size:10px;font-style:italic;line-height:15px;color:#555">In a lorem pellentesque, eleifend metus nec, aliquet lorem. Pellentesque habitant morbi tristique senectus et netus et malesuada fames ac turpis egestas.<br>Nisi ut fringilla nibh condimentum sed. Proin ac blandit dolor. Curabitur ipsum quam ac tristique tincidunt, at pharetra scelerisque.</div>

  <!-- Mirabel tribute -->
  <div class="tribute"></div>
  <svg class="abs" style="left:0;top:2487px" width="460" height="373" viewBox="0 0 460 373"><path d="M0 0H250L460 373H0z" fill="#e5814a"/></svg>
  <div class="abs" role="img" aria-label="Book cover showing an old farmhouse" style="left:217px;top:2550px;width:195px;height:310px;background:linear-gradient(180deg,#d9d2c0,#b8aa8c 55%,#4a2a2a 80%);box-shadow:0 12px 22px rgba(0,0,0,.4)"></div>
  <h2 class="abs script" style="left:445px;top:2530px;font-size:30px;color:#fff">Mirabel</h2>
  <div class="abs" style="left:445px;top:2582px;width:90px;height:2px;background:rgba(255,255,255,.5)"></div>
  <p class="tribute-text">Over the years, our daughters’ friends overlapped one another and two or three became like daughters to Loreen and me. Some even became our friends as they grew into adulthood. One had a father who tried to committed suicide multiple times. After one attempt she asked him, “why?” He said, “I am glad you can’t understand why, only someone who can travel to that dark a place can understand why”. He was eventually successful. She shared that story with us on August 14th when our daughter Mirabel found that dark place in herself and took her life. We found a suicide note, then her body, then everything went into a fog. An hour or so later.</p>
  <span class="btn" style="left:445px;top:2797px">Read More</span>

  <!-- Blog -->
  <h2 class="section-title script" style="top:2940px;color:var(--ink)">Latest Blog</h2>
  <div class="title-rule" style="left:380px;top:2995px;width:440px"></div>
  <svg class="chev" style="left:160px;top:3170px" width="10" height="16" viewBox="0 0 10 16"><path d="M8 1 2 8l6 7" fill="none" stroke="#ccc" stroke-width="2"/></svg>
  <svg class="chev" style="left:1030px;top:3170px" width="10" height="16" viewBox="0 0 10 16"><path d="M2 1l6 7-6 7" fill="none" stroke="#ccc" stroke-width="2"/></svg>
  <article class="blog-card" style="left:210px">
    <div class="thumb" role="img" aria-label="Cyclists on a road below mountains" style="background:linear-gradient(180deg,#8fb2d4,#c8d6e0 35%,#5f7a5a 60%,#8a8a80)"></div>
    <div class="blog-date">Friday 09 Sep 2016</div>
    <div class="blog-title">Lorem ipsum dolor sit amet, amet is adipiscing elit.</div>
    <div class="blog-excerpt">Lorem ipsum dolor sit amet, consectetuer adipiscing elit, sed diam nonummy nibh et euismod tincidunt ut laoreet dolore.</div>
    <div class="blog-more">Read More »</div>
  </article>
  <article class="blog-card" style="left:480px">
    <div class="thumb" role="img" aria-label="Hikers in a meadow beneath peaks" style="background:linear-gradient(180deg,#7fa6cc,#c4d2de 35%,#6b8a4e 60%,#7c9a58)"></div>
    <div class="blog-date">Friday 09 Sep 2016</div>
    <div class="blog-title">Lorem ipsum dolor sit amet, amet is adipiscing elit.</div>
    <div class="blog-excerpt">Lorem ipsum dolor sit amet, consectetuer adipiscing elit, sed diam nonummy nibh et euismod tincidunt ut laoreet dolore.</div>
    <div class="blog-more">Read More »</div>
  </article>
  <article class="blog-card" style="left:750px">
    <div class="thumb" role="img" aria-label="Old wooden barn before a mountain range" style="background:linear-gradient(180deg,#7aa0c8,#c2cfda 35%,#6a5240 60%,#8a9a60)"></div>
    <div class="blog-date">Friday 09 Sep 2016</div>
    <div class="blog-title">Lorem ipsum dolor sit amet, amet is adipiscing elit.</div>
    <div class="blog-excerpt">Lorem ipsum dolor sit amet, consectetuer adipiscing elit, sed diam nonummy nibh et euismod tincidunt ut laoreet dolore.</div>
    <div class="blog-more">Read More »</div>
  </article>
  <span class="btn brown" style="left:548px;top:3378px">View All</span>

  <!-- Footer -->
  <footer class="site-footer"></footer>
  <h3 class="foot-title script" style="left:212px">Quick Links</h3>
  <ul class="foot-list" style="left:212px"><li>Home</li><li>About Me</li><li>Books</li><li>Blog</li><li>Contact Me</li></ul>

  <h3 class="foot-title script" style="left:362px">Contact Info</h3>
  <div class="contact-row" style="top:3548px">HOLLIS<br>1417 Ridgeline Rd Laramie, WY<br>82070
    <svg class="contact-ico" viewBox="0 0 24 24"><circle cx="12" cy="12" r="12" fill="#ef8a4f"/><path d="M12 5a4 4 0 0 0-4 4c0 3 4 9 4 9s4-6 4-9a4 4 0 0 0-4-4zm0 5.5a1.5 1.5 0 1 1 0-3 1.5 1.5 0 0 1 0 3z" fill="#fff"/></svg></div>
  <div class="contact-row" style="top:3608px">307.555.0142
    <svg class="contact-ico" viewBox="0 0 24 24"><circle cx="12" cy="12" r="12" fill="#ef8a4f"/><path d="M9 6l2 3-1.5 1.5a8 8 0 0 0 4 4L15 13l3 2-1 2.5C12 17 7 12 6.5 7z" fill="#fff"/></svg></div>
  <div class="contact-row" style="top:3648px">hello@hollisbooks.example
    <svg class="contact-ico" viewBox="0 0 24 24"><circle cx="12" cy="12" r="12" fill="#ef8a4f"/><rect x="6" y="8" width="12" height="8" fill="#fff"/><path d="M6 8l6 5 6-5" fill="none" stroke="#ef8a4f" stroke-width="1.2"/></svg></div>

  <h3 class="foot-title script" style="left:620px">Newsletter</h3>
  <div class="field" style="top:3555px">Name</div>
  <div class="field" style="top:3593px">E-mail</div>
  <span class="btn" style="left:620px;top:3635px;height:28px;line-height:28px;font-size:10px;padding:0 18px">Subscribe Us Now</span>

  <h3 class="foot-title script" style="left:852px">Follow Me</h3>
  <div class="abs" style="left:880px;top:3552px;width:40px;height:40px;border-radius:50%;background:#8a7a6a"></div>
  <div class="abs script" style="left:862px;top:3600px;font-size:16px;color:#fff">W T Hollis</div>
  <div class="social-dot" style="left:848px"></div>
  <div class="social-dot" style="left:876px"></div>
  <div class="social-dot" style="left:904px"></div>
  <div class="social-dot" style="left:932px"></div>

  <div class="copyright">COPYRIGHT HOLLIS ALL RIGHTS RESERVED</div>
</div>
</body>
</html>
```